Business Card Design Project

Small privately owned salon.

Industry/Entity Type

Business

Contact Information for Business Card

Hair salon.i would like my logo to be my name , Rosalind Marie. Address and phone can go on the front or back. The back will be where I write their appt.
address-527 Willowbend lane Fairhaven, Pa. 17588
Phone- 717-464-3082

```html
<!DOCTYPE html>
<html lang="en">
<head>
<meta charset="utf-8">
<title>Rosalind Marie Hair Salon – Business Card</title>
<link rel="stylesheet" href="https://fonts.googleapis.com/css2?family=Tinos:ital,wght@0,400;0,700;1,400&family=Questrial&display=swap">
<style>
  :root {
    --page-bg: #ecebe8;
    --card-black: #050505;
    --card-white: #ffffff;
    --gold: #c9a15a;
    --text-light: #f4f4f4;
    --ink: #2b2b2b;
    --ink-soft: #3a3a3a;
    --rule: #4a4a4a;
  }
  * { box-sizing: border-box; margin: 0; padding: 0; }
  html, body {
    width: 1012px; height: 1200px; overflow: hidden;
    background: var(--page-bg);
  }
  .card {
    position: absolute; left: 139px; width: 726px; height: 419px;
    box-shadow: 0 4px 14px rgba(0,0,0,0.25);
    overflow: hidden;
  }

  /* Front */
  .card-front { top: 115px; background: var(--card-black); }
  .brand {
    position: absolute; left: 0; right: 0; top: 146px;
    display: flex; align-items: center; justify-content: center; gap: 20px;
  }
  .brand-dot {
    width: 22px; height: 22px; border-radius: 50%; background: var(--gold);
  }
  .brand-text { text-align: center; }
  .brand-name {
    display: block;
    font-family: "Tinos", serif; font-weight: 400;
    color: var(--text-light); font-size: 48px; line-height: 1.05;
  }
  .brand-descriptor {
    display: block; margin-top: 10px;
    font-family: "Tinos", serif; font-weight: 400;
    color: var(--gold); font-size: 21px; letter-spacing: 13px;
    padding-left: 13px;
  }
  .contact-row {
    position: absolute; left: 0; right: 0; top: 347px;
    display: flex; justify-content: center; gap: 34px;
    font-family: "Tinos", serif; font-size: 22px; color: var(--text-light);
  }
  .contact-item { display: flex; align-items: center; gap: 6px; white-space: nowrap; }
  .contact-item svg { width: 18px; height: 22px; fill: var(--gold); }

  /* Back */
  .card-back { top: 651px; background: var(--card-white); }
  .back-strip {
    position: absolute; left: 0; top: 0; bottom: 0; width: 159px;
    background: radial-gradient(ellipse at 55% 35%, #b8a47a 0%, #6e5a38 35%, #1a140c 70%, var(--card-black) 100%);
  }
  .appointment {
    position: absolute; left: 206px; top: 56px; right: 40px; height: 260px;
    font-family: "Questrial", sans-serif; color: var(--ink);
  }
  .appointment-title { font-size: 25px; font-weight: 700; letter-spacing: 0.3px; }
  .field {
    position: absolute; left: 0; display: flex; align-items: flex-end;
    font-size: 19px; color: var(--ink-soft);
  }
  .field-line { display: inline-block; width: 388px; height: 1px; background: var(--rule); margin-left: 4px; margin-bottom: 4px; }
  .field-date { top: 90px; }
  .field-time { top: 160px; }
  .reschedule-note {
    position: absolute; left: 0; top: 229px;
    font-style: italic; font-size: 20px; color: var(--ink-soft); white-space: nowrap;
  }
  .back-phone {
    position: absolute; left: 159px; right: 50px; top: 339px;
    display: flex; justify-content: center; align-items: center; gap: 6px;
    font-family: "Tinos", serif; font-weight: 700; font-size: 27px; color: var(--ink);
  }
  .back-phone svg { width: 22px; height: 24px; fill: var(--ink); }
</style>
</head>
<body>
  <section class="card card-front">
    <div class="brand">
      <span class="brand-dot"></span>
      <div class="brand-text">
        <span class="brand-name">Rosalind Marie</span>
        <span class="brand-descriptor">HAIR SALON</span>
      </div>
    </div>
    <div class="contact-row">
      <span class="contact-item">
        <svg viewBox="0 0 18 24" aria-hidden="true"><path d="M9 0a8 8 0 0 0-8 8c0 6 8 16 8 16s8-10 8-16a8 8 0 0 0-8-8zm0 11a3 3 0 1 1 0-6 3 3 0 0 1 0 6z"/></svg>
        527 Willowbend lane Fairhaven, Pa. 17588
      </span>
      <span class="contact-item">
        <svg viewBox="0 0 24 24" aria-hidden="true"><path d="M6.6 10.8a15 15 0 0 0 6.6 6.6l2.2-2.2a1 1 0 0 1 1-.25 11.4 11.4 0 0 0 3.6.57 1 1 0 0 1 1 1V20a1 1 0 0 1-1 1A17 17 0 0 1 3 4a1 1 0 0 1 1-1h3.5a1 1 0 0 1 1 1c0 1.25.2 2.45.57 3.57a1 1 0 0 1-.25 1z"/></svg>
        717-464-3082
      </span>
    </div>
  </section>

  <section class="card card-back">
    <div class="back-strip" role="img" aria-label="Decorative gold ribbon motif on black"></div>
    <div class="appointment">
      <div class="appointment-title">Appointment:</div>
      <div class="field field-date">Date<span class="field-line"></span></div>
      <div class="field field-time">Time<span class="field-line"></span></div>
      <div class="reschedule-note">If unable to make appointment contact me ASAP</div>
    </div>
    <div class="back-phone">
      <svg viewBox="0 0 24 24" aria-hidden="true"><path d="M6.6 10.8a15 15 0 0 0 6.6 6.6l2.2-2.2a1 1 0 0 1 1-.25 11.4 11.4 0 0 0 3.6.57 1 1 0 0 1 1 1V20a1 1 0 0 1-1 1A17 17 0 0 1 3 4a1 1 0 0 1 1-1h3.5a1 1 0 0 1 1 1c0 1.25.2 2.45.57 3.57a1 1 0 0 1-.25 1z"/></svg>
      717-464-3082
    </div>
  </section>
</body>
</html>
```